Website Design for a High School

School Name: Bayt Qamarin Private Schools
sub-schools:
1-Bayt Qamarin Primary School
2-Bayt Qamarin High School for Girls
3-Bayt Qamarin High School for Boys
The design should be professional and serious and below is the details of the website.
Pages: (Home, About Us, Schools, Events, Students, Gallery, Lectures, Contact Us).
A-) Home Page:
1-Animated photos banner as main
2-Marquee for the last news.
3-Welcoming block of text
4-latest news at the body of the page.
5-Calender "on the side"
6-Number of visitors "on the side"
7-Search bar
8-options to choose a school
B-) School Page:
three schools listed as drop down menu when highlighted over the Schools button in the menu
*Each school page should contain:
1-Student login area
2-Animation photos header
3-Specific news and projects
C-) Student Login page:
have a Report Card
D-) Gallery Page
have a collection of photos.
E-)Contact Page
phone numbers
emails
feedback form
F-)Other mentioned pages
with normal text and photos page look as similar to the Home page.
Required color: Purple as main and include the logo colors
Logo: is attached.
Button link to change language to Arabic.

```html
<!DOCTYPE html>
<html lang="en">
<head>
<meta charset="utf-8">
<title>Bayt Qamarin Private Schools</title>
<link href="https://fonts.googleapis.com/css2?family=Open+Sans:wght@300;400;600;700&display=swap" rel="stylesheet">
<style>
:root{
  --purple:#5a2d8a;
  --purple-dark:#3f1d66;
  --orange:#efa020;
  --orange-dark:#c97f10;
  --teal:#4d6f7c;
  --text:#555;
  --line:#d6d6d6;
  --footer:#ebebeb;
  --footer-bar:#dedede;
}
*{box-sizing:border-box;margin:0;padding:0}
html,body{width:976px;height:1200px;overflow:hidden;background:#fff}
body{font-family:'Open Sans',Arial,sans-serif;color:var(--text);position:relative}
.abs{position:absolute}
.btn{position:absolute;display:flex;align-items:center;justify-content:center;background:linear-gradient(#fff,#ececec);border:1px solid #cfcfcf;border-radius:2px;color:var(--orange-dark);font-size:9px;text-transform:uppercase;box-shadow:0 1px 2px rgba(0,0,0,.15)}
/* header */
.brand-mark{left:80px;top:18px;width:122px;height:122px;border-radius:50%;background:#fff;border:4px solid var(--purple);display:flex;align-items:center;justify-content:center;text-align:center;color:var(--purple);font-size:11px;font-weight:700;line-height:1.3;padding:14px;text-transform:uppercase}
.call-icon{left:374px;top:49px;width:37px;height:37px;border-radius:50%;background:var(--orange);display:flex;align-items:center;justify-content:center}
.call-label{left:422px;top:52px;font-size:11px;font-weight:700;color:#333}
.call-number{left:421px;top:65px;font-size:16px;font-weight:300;color:var(--purple)}
.lang{left:559px;top:54px;width:107px;height:28px;border:1px solid var(--line);font-size:9px;color:#333;display:flex;align-items:center;padding-left:8px}
.lang .flag{width:13px;height:9px;background:#2b3f8a;margin-right:6px;border:1px solid #c33}
.lang .caret{position:absolute;right:8px;top:11px;border:4px solid transparent;border-top-color:#555}
.search{left:676px;top:54px;width:219px;height:28px;border:1px solid var(--line);font-size:9px;color:#333;display:flex;align-items:center;padding-left:11px}
.search svg{position:absolute;right:9px;top:8px}
.main-nav{left:215px;top:103px;width:681px;height:37px;border:1px solid var(--line);display:flex;background:linear-gradient(#fff,#f3f3f3)}
.main-nav a{display:flex;align-items:center;justify-content:center;font-size:10.5px;color:#333;text-decoration:none;border-right:1px solid var(--line);text-transform:uppercase}
.main-nav a:last-child{border-right:0}
.main-nav a.active{background:var(--orange);color:#fff}
/* hero */
.hero{left:80px;top:156px;width:574px;height:343px;background:radial-gradient(circle at 38% 35%,#c7a488 0,#6b6a43 30%,#3e4e2a 60%,#1d2416 100%);overflow:hidden}
.hero-arrow{top:155px;width:33px;height:34px;background:rgba(0,0,0,.25);display:flex;align-items:center;justify-content:center}
.hero-title{left:279px;top:188px;color:#fff;font-size:23px;font-weight:700;letter-spacing:.3px}
.hero-sub{left:279px;top:219px;color:#fff;font-size:14.5px;font-weight:300;letter-spacing:.2px}
.hero .btn{left:279px;top:248px;width:117px;height:32px;font-size:10px}
/* side panels */
.panel{position:absolute;left:664px;width:232px;color:#fff}
.panel .fold{position:absolute;right:0;top:0;width:0;height:0;border-style:solid;border-width:0 21px 21px 0;border-color:transparent #fff transparent transparent}
.panel .fold::after{content:"";position:absolute;left:0;top:0}
.news-panel{top:156px;height:176px;background:var(--purple)}
.news-panel .corner{position:absolute;right:0;top:0;width:21px;height:21px;background:linear-gradient(45deg,var(--purple-dark) 50%,#fff 50%)}
.school-panel{top:345px;height:154px;background:var(--orange)}
.school-panel .corner{position:absolute;right:0;top:0;width:21px;height:21px;background:linear-gradient(45deg,var(--orange-dark) 50%,#fff 50%)}
.panel-head-b{position:absolute;font-size:14px;font-weight:700;letter-spacing:.3px}
.panel-head-l{position:absolute;font-size:19.5px;font-weight:300}
.news-panel p{position:absolute;left:24px;top:72px;width:195px;font-size:9px;line-height:17.5px}
.select-school{position:absolute;left:23px;top:73px;width:188px;height:25px;background:#fff;color:#555;font-size:8.5px;display:flex;align-items:center;padding-left:12px;text-transform:uppercase}
.select-school .caret{position:absolute;right:9px;top:10px;border:4px solid transparent;border-top-color:#555}
/* welcome */
.welcome-title{left:80px;top:524px;font-size:15px;color:var(--purple);font-weight:400}
.welcome-title b,.section-title b{font-weight:700}
.welcome-text{left:80px;top:552px;width:816px;font-size:9px;line-height:19.5px}
.latest{left:80px;top:632px;width:816px;height:38px;border:1px solid var(--line);display:flex;align-items:center}
.latest .label{width:147px;height:100%;background:linear-gradient(#fafafa,#ececec);border-right:1px solid var(--line);display:flex;align-items:center;justify-content:center;font-size:15px;color:#444;font-weight:300}
.latest .ticker{padding-left:15px;font-size:9px;color:#555;word-spacing:.5px}
.latest .ticker span{color:var(--orange-dark)}
/* calendar */
.calendar{left:80px;top:699px;width:260px;height:200px;border:1px solid var(--line);box-shadow:0 1px 2px rgba(0,0,0,.08)}
.cal-head{height:32px;display:flex;align-items:center;justify-content:space-between;border-bottom:1px solid var(--line)}
.cal-head .arrow{width:19px;height:32px;background:var(--teal);display:flex;align-items:center;justify-content:center}
.cal-head .month{font-size:10.5px;font-weight:600;color:#333}
.cal-days{display:grid;grid-template-columns:repeat(7,32px);margin:12px 0 0 16px;font-size:7.5px;font-weight:700;color:#333;text-align:center}
.cal-grid{display:grid;grid-template-columns:repeat(7,32px);grid-auto-rows:24px;margin:8px 0 0 16px;border-top:1px solid #e4e4e4;border-left:1px solid #e4e4e4}
.cal-grid span{display:flex;align-items:center;justify-content:center;font-size:8.5px;color:#333;border-right:1px solid #e4e4e4;border-bottom:1px solid #e4e4e4}
.cal-grid span.muted{color:#ccc}
.cal-grid span.today{background:#a3a66e;color:#fff}
/* about & visitors */
.section-title{font-size:15px;color:var(--purple)}
.about-text{left:374px;top:726px;width:270px;font-size:9px;line-height:19.5px}
.visitors{left:674px;top:703px;font-weight:700}
.visitor-grid{left:674px;top:730px;display:grid;grid-template-columns:repeat(4,50px);grid-auto-rows:49px;gap:4px 6px}
.visitor-grid div{background:linear-gradient(150deg,#d9c3a9,#8a6a55)}
.visitor-grid div:nth-child(2n){background:linear-gradient(150deg,#cfd6de,#7a6a60)}
.visitor-grid div:nth-child(3n){background:linear-gradient(150deg,#e8d6c2,#a07050)}
.visit-count{left:677px;top:845px;font-size:15px;color:#333}
.visit-count b{color:var(--orange);font-weight:700}
/* footer */
.footer{left:0;top:938px;width:976px;height:222px;background:var(--footer)}
.footer-mark{left:92px;top:988px;width:120px;height:120px;border-radius:50%;background:#fff;border:4px solid var(--purple);display:flex;align-items:center;justify-content:center;text-align:center;color:var(--purple);font-size:11px;font-weight:700;line-height:1.3;padding:14px;text-transform:uppercase}
.foot-col{position:absolute;top:976px;font-size:8.5px;color:#555;text-transform:uppercase}
.foot-col h4{font-size:11px;color:var(--purple);font-weight:700;margin-bottom:11px}
.foot-col li{list-style:none;height:18.2px}
.foot-col .c-line{height:18.2px;display:flex;align-items:center;gap:7px}
.foot-col .c-line.gap{height:21.5px}
.social{display:flex;align-items:center;gap:6px;height:35px}
.social i{width:25px;height:25px;border-radius:50%;display:block}
.bottom-bar{left:0;top:1160px;width:976px;height:40px;background:var(--footer-bar);display:flex;align-items:center;justify-content:center;font-size:8.5px;color:#555}
</style>
</head>
<body>

<header>
  <div class="abs brand-mark">Bayt Qamarin Private Schools</div>
  <div class="abs call-icon">
    <svg width="16" height="16" viewBox="0 0 24 24"><path fill="#fff" d="M6.6 10.8a15.2 15.2 0 0 0 6.6 6.6l2.2-2.2c.3-.3.7-.4 1-.2 1.1.4 2.3.6 3.6.6.6 0 1 .4 1 1V20c0 .6-.4 1-1 1A17 17 0 0 1 3 4c0-.6.4-1 1-1h3.5c.6 0 1 .4 1 1 0 1.3.2 2.5.6 3.6.1.3 0 .7-.2 1z"/></svg>
  </div>
  <div class="abs call-label">CALL US :</div>
  <div class="abs call-number">( 2480 ) 317 904</div>
  <div class="abs lang"><span class="flag"></span>ENGLISH<span class="caret"></span></div>
  <div class="abs search">SEARCH
    <svg width="12" height="12" viewBox="0 0 12 12"><circle cx="5" cy="5" r="3.8" fill="none" stroke="#999" stroke-width="1.3"/><line x1="7.8" y1="7.8" x2="11" y2="11" stroke="#999" stroke-width="1.5"/></svg>
  </div>
  <nav class="abs main-nav">
    <a class="active" style="width:72px">Home</a>
    <a style="width:90px">About Us</a>
    <a style="width:84px">Schools</a>
    <a style="width:74px">Events</a>
    <a style="width:91px">Students</a>
    <a style="width:81px">Gallery</a>
    <a style="width:84px">Lectures</a>
    <a style="width:103px">Contact Us</a>
  </nav>
</header>

<section class="abs hero" role="img" aria-label="Smiling graduate in cap and gown giving a thumbs up, classmates blurred behind">
  <div class="abs hero-arrow" style="left:0"><svg width="10" height="18"><polyline points="8,1 2,9 8,17" fill="none" stroke="#ddd" stroke-width="1.3"/></svg></div>
  <div class="abs hero-arrow" style="right:0"><svg width="10" height="18"><polyline points="2,1 8,9 2,17" fill="none" stroke="#ddd" stroke-width="1.3"/></svg></div>
  <div class="abs hero-title">LOREM IPSUM IS</div>
  <div class="abs hero-sub">SIMPLY DUMMY TEXT OF THE PRINTING</div>
  <div class="btn">Joined Now</div>
</section>

<aside class="panel news-panel">
  <div class="corner"></div>
  <svg class="abs" style="left:24px;top:22px" width="30" height="36" viewBox="0 0 30 36"><path d="M2 2h18l8 8v24H2z" fill="#fff"/><path d="M20 2v8h8" fill="#ddd"/><rect x="7" y="15" width="16" height="2.5" fill="var(--purple)"/><rect x="7" y="21" width="16" height="2.5" fill="var(--purple)"/><rect x="7" y="27" width="16" height="2.5" fill="var(--purple)"/></svg>
  <div class="panel-head-b" style="left:63px;top:18px">MARQUEE FOR</div>
  <div class="panel-head-l" style="left:63px;top:35px">THE LAST NEWS</div>
  <p>Lorem Ipsum is simply dummy text of the printing and typesetting industry. Lorem Ipsum has been the industry's...</p>
  <div class="btn" style="left:115px;top:133px;width:96px;height:26px;font-size:8.5px">View More News</div>
</aside>

<aside class="panel school-panel">
  <div class="corner"></div>
  <svg class="abs" style="left:23px;top:22px" width="46" height="34" viewBox="0 0 46 34"><polygon points="23,2 45,11 23,20 1,11" fill="#fff"/><path d="M11 15v9c4 4 20 4 24 0v-9l-12 5z" fill="#fff"/><line x1="40" y1="13" x2="40" y2="26" stroke="#fff" stroke-width="1.5"/></svg>
  <div class="panel-head-b" style="left:74px;top:18px">SELECT</div>
  <div class="panel-head-l" style="left:74px;top:35px">A SCHOOL</div>
  <div class="select-school">Bayt Qamarin Primary School<span class="caret"></span></div>
  <div class="btn" style="left:23px;top:110px;width:188px;height:26px;font-size:8.5px">View Info For The Selected School</div>
</aside>

<main>
  <h1 class="abs welcome-title">WELCOME TO <b>BAYT QAMARIN SCHOOLS</b></h1>
  <p class="abs welcome-text">Lorem Ipsum is simply dummy text of the printing and typesetting industry. Lorem Ipsum has been the industry's standard dummy text ever since the 1500s, when an unknown printer took a galley of type and scrambled it to make a type specimen book. It has survived not only five centuries, but also the leap into electronic typesetting, remaining essentially unchanged. It was popularised in the 1960s with the release of Letraset sheets containing Lorem Ipsum passages...</p>

  <div class="abs latest">
    <div class="label">LATEST NEWS</div>
    <div class="ticker">Lorem Ipsum is simply dummy text of the printing and typesetting industry. &nbsp;&nbsp;&nbsp; Ipsum has been the industry's standard dummy text... <span>[ Read More ]</span></div>
  </div>

  <div class="abs calendar">
    <div class="cal-head">
      <div class="arrow"><svg width="7" height="10"><polyline points="6,1 2,5 6,9" fill="none" stroke="#fff" stroke-width="1.8"/></svg></div>
      <div class="month">NOVEMBER</div>
      <div class="arrow"><svg width="7" height="10"><polyline points="1,1 5,5 1,9" fill="none" stroke="#fff" stroke-width="1.8"/></svg></div>
    </div>
    <div class="cal-days"><span>Mon</span><span>Tue</span><span>Wed</span><span>Thu</span><span>Fri</span><span>Sat</span><span>Sun</span></div>
    <div class="cal-grid">
      <span>1</span><span>2</span><span>3</span><span>4</span><span>5</span><span>6</span><span>7</span>
      <span>8</span><span>9</span><span>10</span><span>11</span><span>12</span><span>13</span><span>14</span>
      <span>15</span><span>16</span><span>17</span><span>18</span><span>19</span><span>20</span><span>21</span>
      <span>22</span><span>23</span><span>24</span><span>25</span><span>26</span><span>27</span><span>28</span>
      <span>29</span><span class="today">30</span><span>31</span><span class="muted">1</span><span class="muted">2</span><span class="muted">3</span><span class="muted">4</span>
    </div>
  </div>

  <h2 class="abs section-title" style="left:374px;top:693px;font-weight:400">ABOUT <b>BAYT QAMARIN SCHOOLS</b></h2>
  <p class="abs about-text">Lorem Ipsum is simply dummy text of the printing and typesetting industry. Lorem Ipsum has been the industry's standard dummy text ever since the 1500s, when an unknown printer took a galley of type and scrambled.<br><br>it to make a type specimen book. It has survived not only five centuries, but also the leap into electronic...</p>
  <div class="btn" style="left:374px;top:874px;width:108px;height:29px">View More Info</div>

  <h2 class="abs section-title visitors" style="top:693px">VISITORS</h2>
  <div class="abs visitor-grid" role="img" aria-label="Eight small portrait photos of recent visitors">
    <div></div><div></div><div></div><div></div><div></div><div></div><div></div><div></div>
  </div>
  <div class="abs visit-count">620 <b>USERS VISIT ONLINE</b></div>
  <div class="btn" style="left:674px;top:874px;width:108px;height:29px">View More Info</div>
</main>

<footer>
  <div class="abs footer"></div>
  <div class="abs footer-mark">Bayt Qamarin Private Schools</div>

  <div class="foot-col" style="left:283px">
    <h4>WELCOME</h4>
    <ul><li>Home</li><li>About Us</li><li>Schools</li><li>Events</li><li>Students</li><li>Gallery</li><li>Lectures</li><li>Contact Us</li></ul>
  </div>

  <div class="foot-col" style="left:429px">
    <h4>CONTACT</h4>
    <div class="c-line">Bayt Qamarin Schools</div>
    <div class="c-line">120 Street Name, City Name,</div>
    <div class="c-line gap">Country Name : 48105530</div>
    <div class="c-line gap"><svg width="8" height="11"><rect x="1" y="0.5" width="6" height="10" rx="1" fill="none" stroke="#666"/></svg>( 2480 ) 317 552</div>
    <div class="c-line gap"><svg width="10" height="9"><rect x="0" y="3" width="10" height="5" fill="#666"/><rect x="2" y="0" width="6" height="3" fill="#666"/></svg>( 2480 ) 317 552</div>
    <div class="c-line" style="text-transform:none"><svg width="10" height="8"><rect x=".5" y=".5" width="9" height="7" fill="none" stroke="#666"/><polyline points=".5,.5 5,5 9.5,.5" fill="none" stroke="#666"/></svg>info@baytqamarinschools.example</div>
  </div>

  <div class="foot-col" style="left:646px">
    <h4>INFORMATION</h4>
    <ul><li>Privacy Policy</li><li>Terms &amp; Conditions</li><li>Sitemap</li></ul>
  </div>

  <div class="foot-col" style="left:799px">
    <h4>FOLLOW US</h4>
    <div class="social"><i style="background:#2f55a4"></i>: Circlepage</div>
    <div class="social"><i style="background:#3fa9e0"></i>: Chirpline</div>
    <div class="social"><i style="background:#1d6fa5"></i>: Worklinks</div>
  </div>

  <div class="abs bottom-bar">© 2015. BAYT QAMARIN SCHOOLS. ALL RIGHTS RESERVED.</div>
</footer>

</body>
</html>
```